Business Card Design

Please see my website www.lqvesting.com.au to for further information on my services and styling of my site

Project Deadline Extended
Reason: Deadline is extended to permit alterations to current designs or for any new submissions. Cheers

Industry/Entity Type

Business

Contact Information for Business Card

Marcus Theale
Empowerment Coach

'Live your passion'

marcus@lqvcoaching.com.au
0437518264
lqvcoaching.com.au

```html
<!DOCTYPE html>
<html lang="en">
<head>
<meta charset="utf-8">
<title>Business Card – Marcus Theale</title>
<link rel="stylesheet" href="https://fonts.googleapis.com/css2?family=Josefin+Sans:wght@300;400;700&family=Dancing+Script&display=swap">
<style>
  :root {
    --bg-light: #f2f2f2;
    --bg-dark: #9a9a9a;
    --card: #262525;
    --card-edge: #1b1a1a;
    --lime: #b8d430;
    --lime-soft: #a7bf2e;
    --ink-light: #d9d9d9;
    --white: #ffffff;
  }
  * { box-sizing: border-box; margin: 0; padding: 0; }
  html, body { width: 1200px; height: 900px; overflow: hidden; }
  body {
    background: radial-gradient(ellipse at 55% 45%, var(--bg-light) 0%, #d0d0d0 45%, var(--bg-dark) 100%);
    font-family: "Josefin Sans", sans-serif;
    position: relative;
  }
  .card {
    position: absolute;
    left: 255px;
    width: 690px;
    height: 394px;
    border-radius: 22px;
    background: linear-gradient(160deg, #2e2d2d 0%, var(--card) 50%, var(--card-edge) 100%);
    box-shadow: 0 14px 30px rgba(0,0,0,0.35);
    overflow: hidden;
  }
  .card--front { top: 40px; }
  .card--back { top: 466px; }

  /* front */
  .front-brand {
    position: absolute;
    left: 70px;
    top: 150px;
    display: flex;
    align-items: center;
    gap: 28px;
  }
  .brand-square {
    width: 96px;
    height: 96px;
    background: var(--white);
  }
  .front-brand__name {
    color: var(--lime);
    font-weight: 700;
    font-size: 30px;
    letter-spacing: 0.5px;
  }

  /* back */
  .tagline {
    position: absolute;
    left: 210px;
    top: 40px;
    font-family: "Dancing Script", cursive;
    font-size: 46px;
    color: var(--lime);
    transform: rotate(9deg);
    transform-origin: left center;
    letter-spacing: 3px;
  }
  .back-brand {
    position: absolute;
    right: 40px;
    top: 36px;
    text-align: right;
    border-bottom: 2px solid var(--white);
    padding-bottom: 6px;
  }
  .back-brand__mark {
    color: var(--lime);
    font-weight: 700;
    font-size: 34px;
    letter-spacing: 2px;
  }
  .back-brand__name {
    color: var(--lime);
    font-weight: 700;
    font-size: 14px;
  }
  .identity {
    position: absolute;
    left: 48px;
    top: 140px;
  }
  .identity__name {
    color: var(--lime);
    font-weight: 300;
    font-size: 44px;
    letter-spacing: 2px;
  }
  .identity__role {
    color: var(--lime-soft);
    font-weight: 300;
    font-size: 14px;
    letter-spacing: 3px;
    text-transform: uppercase;
    margin-top: 2px;
    padding-left: 24px;
  }
  .divider {
    position: absolute;
    left: 372px;
    top: 228px;
    width: 2px;
    height: 80px;
    background: linear-gradient(to bottom, transparent, var(--lime-soft), transparent);
  }
  .contact {
    position: absolute;
    left: 420px;
    top: 256px;
    list-style: none;
    font-size: 17px;
    line-height: 1.3;
  }
  .contact__label { color: var(--lime); font-weight: 400; }
  .contact__value { color: var(--ink-light); font-weight: 300; letter-spacing: 1px; }
</style>
</head>
<body>
  <section class="card card--front" aria-label="Card front">
    <div class="front-brand">
      <div class="brand-square"></div>
      <span class="front-brand__name">Life Quest Vitality Coaching</span>
    </div>
  </section>

  <section class="card card--back" aria-label="Card back">
    <p class="tagline">Live your passion</p>
    <div class="back-brand">
      <div class="back-brand__mark">LQV</div>
      <div class="back-brand__name">Life Quest Vitality Coaching</div>
    </div>
    <div class="identity">
      <h1 class="identity__name">Marcus Theale</h1>
      <p class="identity__role">Empowerment Coach</p>
    </div>
    <div class="divider"></div>
    <ul class="contact">
      <li><span class="contact__label">phone:</span> <span class="contact__value">0437518264</span></li>
      <li><span class="contact__label">email:</span> <span class="contact__value">marcus@lqvcoaching.com.au</span></li>
      <li><span class="contact__label">web:</span> <span class="contact__value">lqvcoaching.com.au</span></li>
    </ul>
  </section>
</body>
</html>
```